依頼詳細
PCとスマホデザインの両方納品をいただきますが、
まずはデザインイメージが確認しやすいPCページのみの提案をお願いします。
スマホページは当選者に納品時にお願いしたいと思います。
スマホサイズは横幅750pxのサイズで作成してください。

レスポンシブウェブデザインを意識したデザインでお願いします。

デザインに関しては、添付してあるデザインレイアウト設計シートを基にお願いします。
参考サイトのURLはデザインレイアウト設計シートに記載してあります。

画像データについては、既存サイトや参考サイト、フリー素材から流用してイメージ画像に当て込んでください。
足りない場合は、一旦他のサイトの写真をサンプルとして入れてください。(サンプルなどの表記をお願いします)
ページ数
1ページ
希望イメージ
シンプル 複雑
単色 カラフル
暗い 明るい
日常 高級
遊び心 厳粛
未来的 伝統的
女性的 男性的
希望する色
青系、水色系、明るい色味
納品ファイル
• 高解像度JPG (.jpg)
• イラストレーター形式 (.ai)
• フォトショップ形式 (.psd)
• PNG形式 (.png)
補足説明
上記のいずれか1つ。アウトラインありとなしの2つ。

クライアントのイメージ通りでした。

たくさんのご提案ありがとうございました。
次回もぜひ、よろしくお願い致します。

```html
<!DOCTYPE html>
<html lang="ja">
<head>
<meta charset="utf-8">
<title>ルミナ・インダストリー</title>
<link href="https://fonts.googleapis.com/css2?family=Noto+Sans+JP:wght@400;500;700&family=M+PLUS+Rounded+1c:wght@500;700&display=swap" rel="stylesheet">
<style>
:root{
  --blue:#1f8fd6;
  --cyan:#46bfe3;
  --sky:#d9eff8;
  --sky-deep:#bfe4f3;
  --orange:#f29a3a;
  --orange-soft:#fbe6cc;
  --beige:#f6e6cc;
  --ink:#333;
  --muted:#777;
  --line:#cfcfcf;
  --green:#3aa64a;
  --footer:#4b6470;
  --footer-dark:#3d535d;
  --red:#d93030;
  --tel:#e0364a;
}
*{box-sizing:border-box;margin:0;padding:0}
html,body{width:1200px;height:3240px;overflow:hidden}
body{font-family:"Noto Sans JP",sans-serif;color:var(--ink);background:#fff;position:relative}
a{color:inherit;text-decoration:none}
ul{list-style:none}

.site-header{height:112px;display:flex;align-items:center;padding:0 40px;gap:24px;border-bottom:4px solid var(--sky-deep)}
.brand{display:flex;align-items:center;gap:12px;font-weight:700;font-size:34px;color:var(--blue);letter-spacing:2px;white-space:nowrap}
.brand-dot{width:22px;height:22px;border-radius:50%;background:var(--cyan)}
.global-nav{display:flex;gap:6px;margin-left:40px}
.global-nav a{background:var(--cyan);color:#fff;font-size:15px;padding:10px 16px;border-radius:2px;white-space:nowrap}
.search{margin-left:auto;display:flex;gap:6px}
.search span{width:72px;height:40px;background:var(--sky);border:1px solid var(--cyan);display:flex;align-items:center;justify-content:center;font-size:15px;color:var(--blue)}

.hero{position:relative;height:688px}
.hero-photo{position:absolute;inset:0;background:
  radial-gradient(ellipse 420px 380px at 30% 45%,#fbf3ea 0%,rgba(251,243,234,0) 70%),
  radial-gradient(ellipse 300px 260px at 75% 25%,#e7d7d3 0%,rgba(231,215,211,0) 70%),
  radial-gradient(ellipse 260px 300px at 88% 70%,#c9dbe4 0%,rgba(201,219,228,0) 70%),
  linear-gradient(120deg,#eef1f3 0%,#f4efe8 40%,#e2e8ec 70%,#d3dde2 100%)}
.hero-copy{position:absolute;left:60px;top:430px}
.hero-copy p{display:inline-block;background:rgba(31,143,214,.8);color:#fff;font-size:46px;font-weight:700;padding:4px 16px;margin-bottom:10px;letter-spacing:2px;white-space:nowrap}
.hero-btn{position:absolute;left:440px;top:630px;background:#fff;border:2px solid var(--cyan);font-size:22px;padding:10px 32px;border-radius:4px;white-space:nowrap}
.hero-contact{position:absolute;right:36px;top:580px;background:#fff;border:3px solid var(--orange);color:var(--orange);font-size:28px;font-weight:700;padding:18px 20px;border-radius:6px;white-space:nowrap}

.section-rule{height:24px;background:var(--orange-soft);border-top:3px solid var(--orange);border-bottom:3px solid var(--orange)}
.section-title{display:block;width:250px;margin:28px auto;background:var(--cyan);color:#fff;text-align:center;font-size:30px;font-weight:500;padding:10px 0}

.products{background:var(--sky);height:400px;position:relative;padding-top:40px}
.carousel{display:flex;justify-content:center;gap:40px}
.product{width:210px;text-align:center}
.product-img{height:200px;border:1px solid #b9d8e5}
.product-label{margin:14px 0 8px;background:#fff;border:1px solid var(--line);font-size:18px;padding:8px 0;white-space:nowrap}
.product-cap{font-size:13px;color:var(--muted);white-space:nowrap}
.arrow{position:absolute;top:130px;font-size:80px;color:var(--orange);font-weight:700;line-height:1}
.arrow.left{left:40px}.arrow.right{right:40px}
.dots{display:flex;justify-content:center;gap:14px;margin-top:20px}
.dots i{width:26px;height:26px;border-radius:50%;background:#bbb;display:block}
.dots i.on{background:var(--red)}

.more-btn{display:block;width:300px;margin:60px auto 50px;border:2px solid #999;text-align:center;font-size:20px;padding:12px 0;background:#fff;white-space:nowrap}

.news{width:1040px;margin:0 auto}
.news-row{display:flex;align-items:center;height:80px;border-bottom:2px solid var(--line);font-size:26px;white-space:nowrap}
.news-date{width:200px;padding-left:12px}
.news-cat{width:130px;font-size:17px}
.news .more-btn{margin:40px auto 60px}

.links{background:var(--beige);height:560px;position:relative}
.shop-banner{position:absolute;left:96px;top:50px;width:1008px;height:220px;background:#fff;border:2px solid #e0cfb2;display:flex}
.shop-logo{width:520px;padding:30px 40px}
.shop-name{font-size:50px;font-weight:700;color:var(--green);white-space:nowrap}
.shop-sub{font-size:22px;color:var(--ink);margin-top:6px;letter-spacing:2px}
.shop-img{flex:1;margin:20px;background:linear-gradient(135deg,#dfe9f2,#f2f6f9 60%,#e6c9c9)}
.catalog-btn{position:absolute;left:96px;top:330px;width:290px;height:110px;background:var(--green);color:#fff;font-size:26px;font-weight:700;display:flex;align-items:center;justify-content:center;border-radius:6px;text-align:center}
.company-img{position:absolute;left:700px;top:310px;width:230px;height:170px;background:linear-gradient(180deg,#d9eaf5,#a9c4d2)}
.company-link{position:absolute;left:940px;top:410px;font-size:38px;color:var(--ink);white-space:nowrap}

.contact{height:240px;display:flex;align-items:center;padding:0 60px;background:linear-gradient(180deg,#fff,var(--sky))}
.faq{display:flex;align-items:center;gap:16px;font-size:46px;font-weight:700;color:var(--cyan);font-family:"M PLUS Rounded 1c",sans-serif;white-space:nowrap}
.faq-icon{width:110px;height:110px;border-radius:50%;background:linear-gradient(135deg,#7fd07a,#46bfe3)}
.tel-block{margin-left:auto;width:470px}
.tel-head{background:var(--sky-deep);font-size:28px;text-align:center;padding:4px 0;margin-bottom:8px}
.tel-block p{font-size:50px;color:var(--tel);line-height:1.15;letter-spacing:1px;white-space:nowrap}

.site-footer{background:var(--footer);color:#fff;height:330px;padding:34px 60px 0;display:flex;position:relative}
.foot-col{width:340px;font-size:19px;line-height:1.55;white-space:nowrap}
.foot-info{margin-left:auto;width:380px;font-size:15px;line-height:1.55}
.foot-brand{display:flex;align-items:center;gap:12px;font-size:38px;font-weight:700;margin-bottom:14px}
.foot-brand span{width:22px;height:22px;border-radius:50%;background:#fff;display:block}
.copyright{position:absolute;left:0;right:0;bottom:0;height:44px;background:var(--footer-dark);text-align:center;font-size:16px;line-height:44px}
</style>
</head>
<body>
<header class="site-header">
  <div class="brand"><span class="brand-dot"></span>LUMINA</div>
  <nav class="global-nav">
    <a href="#">ルミナ・インダストリーとは</a><a href="#">商品一覧</a><a href="#">部署長ギャベ</a><a href="#">WEBカタログ</a><a href="#">会社案内</a>
  </nav>
  <div class="search"><span>検索</span><span>Q</span></div>
</header>

<section class="hero">
  <div class="hero-photo" role="img" aria-label="笑顔の女性と日用品の写真コラージュ"></div>
  <div class="hero-copy"><p>ルミナ・インダストリーの商品が</p><br><p>日々の生活に新提案</p></div>
  <a class="hero-btn" href="#">ルミナ・インダストリーとは　›</a>
  <a class="hero-contact" href="#">お問い合わせ</a>
</section>

<div class="section-rule"></div>
<h2 class="section-title">商品紹介</h2>
<section class="products">
  <span class="arrow left">«</span><span class="arrow right">»</span>
  <div class="carousel">
    <div class="product"><div class="product-img" role="img" aria-label="ポータブルファンの写真" style="background:linear-gradient(#cfe3ee,#8fb3c6)"></div><div class="product-label">アイデア商品</div><p class="product-cap">折りたたみ式 小型ファン</p></div>
    <div class="product"><div class="product-img" role="img" aria-label="収納コンテナの写真" style="background:linear-gradient(#eef2f4,#5b6670)"></div><div class="product-label">収納用品</div><p class="product-cap">スタックコンテナ</p></div>
    <div class="product"><div class="product-img" role="img" aria-label="防護マスクの写真" style="background:linear-gradient(#f3f7fb,#6fa7d8)"></div><div class="product-label">保護用品 / 防犯用品</div><p class="product-cap">防じんマスク 交換フィルター付</p></div>
    <div class="product"><div class="product-img" role="img" aria-label="LEDヘッドライトの写真" style="background:linear-gradient(#f4f4f4,#7c7c7c)"></div><div class="product-label">LED 商品</div><p class="product-cap">LEDヘッドライト</p></div>
  </div>
  <div class="dots"><i class="on"></i><i></i><i></i><i></i><i></i></div>
</section>
<a class="more-btn" href="#">商品一覧はこちら　›</a>

<div class="section-rule"></div>
<h2 class="section-title">お知らせ</h2>
<section class="news">
  <div class="news-row"><span class="news-date">2020/10/30</span><span class="news-cat">お知らせ</span><span>ホームページを改訂しました。</span></div>
  <div class="news-row"><span class="news-date">2020/09/29</span><span class="news-cat">新着情報</span><span>LED 証明の新商品が入荷しました。</span></div>
  <div class="news-row"><span class="news-date">2020/08/27</span><span class="news-cat">お知らせ</span><span>ハレマ市場の送料が改定になりました。</span></div>
  <div class="news-row"><span class="news-date">2020/07/20</span><span class="news-cat">お知らせ</span><span>カタログをご利用いただけるようになりました。</span></div>
  <a class="more-btn" href="#">お知らせ一覧はこちら　›</a>
</section>

<section class="links">
  <a class="shop-banner" href="#">
    <div class="shop-logo"><p class="shop-name">ポプラショップ</p><p class="shop-sub">INTERIOR LIFESTYLE GOODS<br>– ハレマ市場店 –</p></div>
    <div class="shop-img" role="img" aria-label="配送トラックと送料無料の案内画像"></div>
  </a>
  <a class="catalog-btn" href="#">Webカタログは<br>こちらから</a>
  <div class="company-img" role="img" aria-label="会社社屋の外観写真"></div>
  <a class="company-link" href="#">会社案内 ›</a>
</section>

<section class="contact">
  <a class="faq" href="#"><span class="faq-icon" role="img" aria-label="質問と回答の吹き出しイラスト"></span>よくあるご質問</a>
  <div class="tel-block">
    <div class="tel-head">お問い合わせ</div>
    <p>TEL 0120-45-6781</p>
    <p>FAX 0120-45-6782</p>
  </div>
</section>

<footer class="site-footer">
  <ul class="foot-col">
    <li>HOME</li><li>ルミナ・インダストリーとは</li><li>商品一覧</li><li>部署長ギャベ</li><li>WEBカタログ</li><li>会社案内</li>
  </ul>
  <ul class="foot-col">
    <li>お問い合わせ</li><li>よくあるご質問</li><li>リンク</li><li>個人情報保護方針</li><li>サイトマップ</li>
  </ul>
  <div class="foot-info">
    <div class="foot-brand"><span></span>LUMINA</div>
    <p>ルミナ・インダストリー株式会社</p>
    <p>〒000-0000</p>
    <p>みどり県青葉市中央町1丁目3番9号</p>
    <p>TEL:0120-45-6781</p>
    <p>FAX:0120-45-6782</p>
  </div>
  <p class="copyright">© Copyright LUMINA-INDUSTRY co.,ltd. All Rights Reserved.</p>
</footer>
</body>
</html>
```